Uk Sports Coaching company needs a poster design for a new 'Speed Development Centre'

We need a poster design for my UK based company called 'Brisk Field Academy'. We are a sports coaching company who specialise in rugby coaching and athlete development. We need a poster design that is quite modern, which explains all about our new venture which is our 'Speed Development Centre'.

The poster needs to explain what will be coached at the centre: Balance, Speed of limb movement, trunk strength, explosive strength, running speed, agility and anaerobic capacity. (these can be bullet pointed).

The poster should include:

When: Starting Friday 3rd October @6pm-7pm (Then every following Friday

venue: Harwick Grange Athletics Track

Price: £100 for the full course + free training T-Shirt

I would also like it to say how to book and get in contact through my phone number and email address which are:

contact@briskfieldacademy.co.uk

07700914386

www.briskfieldacademy.com

Our company colours are black, red and white, and that is also the colour of our logo.

Speed Development centre is open to all players aged 8-16.

I have attached multiple copies of my logo in different formats, i have also attached a word document briefly explaining what the speed development centre will achieve.

Thank you!

Target Market(s)

Parents and Aspiring Rugby players

Industry/Entity Type

Training

Requirements
Must have
• Price
Venue
When it will commence

```html
<!DOCTYPE html>
<html lang="en">
<head>
<meta charset="utf-8">
<title>Speed Development Centre – Brisk Field Academy</title>
<link rel="stylesheet" href="https://fonts.googleapis.com/css2?family=Oswald:wght@500;700&family=Open+Sans:wght@400;600;700&display=swap">
<style>
  :root {
    --red: #d4202a;
    --red-dark: #8e0f16;
    --black: #121212;
    --charcoal: #2a2a2a;
    --white: #ffffff;
    --light: #eeeeee;
    --photo-green: #5c7a3a;
    --photo-sky: #9aa69a;
  }
  * { box-sizing: border-box; margin: 0; padding: 0; }
  html, body { width: 900px; height: 1200px; overflow: hidden; background: #d9d9d9; }
  .poster {
    position: relative; width: 900px; height: 1200px; overflow: hidden;
    background: linear-gradient(180deg, #1c1c1c 0%, var(--black) 60%, #1a1a1a 100%);
    font-family: "Open Sans", Arial, sans-serif; color: var(--white);
  }
  .title-band {
    position: absolute; left: 0; top: 42px; width: 900px; height: 92px;
    background: linear-gradient(180deg, #e8333c 0%, var(--red) 50%, var(--red-dark) 100%);
    border-top: 3px solid var(--white); border-bottom: 3px solid var(--white);
    display: flex; align-items: center; justify-content: center;
  }
  .title-band h1 {
    font-family: "Oswald", Arial, sans-serif; font-weight: 700; font-size: 56px;
    letter-spacing: 2px; text-transform: uppercase; color: var(--white);
  }
  .photo-hero {
    position: absolute; left: 30px; top: 160px; width: 560px; height: 600px;
    background: linear-gradient(180deg, var(--photo-sky) 0%, #7d8c6a 40%, var(--photo-green) 70%, #3f5a2a 100%);
  }
  .info-panel {
    position: absolute; left: 520px; top: 250px; width: 350px; height: 500px;
    clip-path: polygon(60px 0, 100% 0, 100% 100%, 0 100%);
    background: linear-gradient(160deg, #e23540 0%, var(--red) 45%, var(--red-dark) 100%);
  }
  .brand-strip {
    position: absolute; left: 580px; top: 280px; width: 290px; height: 110px;
    background: linear-gradient(180deg, var(--white), var(--light));
    clip-path: polygon(30px 0, 100% 0, 100% 100%, 0 100%);
    display: flex; align-items: center; justify-content: center; gap: 12px;
  }
  .brand-strip .brand-dot { width: 22px; height: 22px; border-radius: 50%; background: var(--red); }
  .brand-strip .brand-name {
    font-family: "Oswald", Arial, sans-serif; font-weight: 500; font-size: 26px; color: var(--black);
  }
  .info-text { position: absolute; left: 600px; top: 415px; width: 255px; }
  .info-text .intro { font-size: 19px; line-height: 1.3; margin-bottom: 18px; }
  .info-text h2 { font-size: 22px; font-weight: 700; margin-bottom: 8px; }
  .session-list { list-style: none; }
  .session-list li { display: flex; align-items: center; gap: 10px; font-size: 19px; line-height: 1.45; }
  .session-list svg { width: 18px; height: 18px; flex: none; }
  .price-badge {
    position: absolute; left: 305px; top: 600px; width: 190px; height: 190px; border-radius: 50%;
    background: radial-gradient(circle at 40% 35%, var(--white) 60%, #d8d8d8 100%);
    border: 4px solid var(--red); color: var(--red);
    display: flex; flex-direction: column; align-items: center; justify-content: center; text-align: center;
  }
  .price-badge .amount { font-family: "Oswald", Arial, sans-serif; font-weight: 700; font-size: 62px; line-height: 1; }
  .price-badge .detail { font-size: 14px; font-weight: 600; line-height: 1.2; color: var(--red-dark); }
  .price-badge .note { font-size: 12px; color: var(--charcoal); margin-top: 3px; }
  .details { position: absolute; left: 30px; top: 790px; width: 520px; }
  .detail-bar {
    display: flex; align-items: flex-start; gap: 18px; padding: 12px 18px;
    background: linear-gradient(90deg, var(--red) 0%, var(--red-dark) 100%);
    margin-bottom: 10px;
  }
  .detail-bar .label { font-family: "Oswald", Arial, sans-serif; font-weight: 700; font-size: 44px; line-height: 1; }
  .detail-bar .value { font-size: 22px; font-weight: 700; line-height: 1.2; padding-top: 2px; }
  .detail-bar .value small { display: block; font-size: 16px; font-weight: 400; }
  .booking { position: absolute; left: 50px; top: 1000px; width: 480px; }
  .booking .cta { font-size: 24px; line-height: 1.2; color: var(--red); margin-bottom: 18px; }
  .booking .cta strong { font-weight: 700; }
  .contact-list { list-style: none; }
  .contact-list li { display: flex; align-items: center; gap: 12px; font-size: 18px; line-height: 1.7; }
  .contact-list svg { width: 20px; height: 20px; flex: none; }
  .photo-action {
    position: absolute; left: 560px; top: 770px; width: 310px; height: 390px;
    clip-path: polygon(40px 0, 100% 0, 100% 100%, 0 100%);
    background: linear-gradient(180deg, #6f7d5c 0%, var(--photo-green) 45%, #3c5528 100%);
  }
</style>
</head>
<body>
<div class="poster">
  <header class="title-band"><h1>Speed Development Centre</h1></header>

  <div class="photo-hero" role="img" aria-label="Photo of young rugby players running with the ball on a grass pitch"></div>

  <div class="info-panel"></div>
  <div class="brand-strip">
    <span class="brand-dot"></span>
    <span class="brand-name">Brisk Field Academy</span>
  </div>

  <section class="info-text">
    <p class="intro">The speed development centre is open to all players aged 8-16.</p>
    <h2>Sessions will cover:</h2>
    <ul class="session-list">
      <li><svg viewBox="0 0 20 20"><path d="M3 10l5 5 9-11" fill="none" stroke="#fff" stroke-width="3"/></svg>Balance</li>
      <li><svg viewBox="0 0 20 20"><path d="M3 10l5 5 9-11" fill="none" stroke="#fff" stroke-width="3"/></svg>Speed of limb movement</li>
      <li><svg viewBox="0 0 20 20"><path d="M3 10l5 5 9-11" fill="none" stroke="#fff" stroke-width="3"/></svg>Trunk strength</li>
      <li><svg viewBox="0 0 20 20"><path d="M3 10l5 5 9-11" fill="none" stroke="#fff" stroke-width="3"/></svg>Explosive strength</li>
      <li><svg viewBox="0 0 20 20"><path d="M3 10l5 5 9-11" fill="none" stroke="#fff" stroke-width="3"/></svg>Running speed</li>
      <li><svg viewBox="0 0 20 20"><path d="M3 10l5 5 9-11" fill="none" stroke="#fff" stroke-width="3"/></svg>Agility</li>
      <li><svg viewBox="0 0 20 20"><path d="M3 10l5 5 9-11" fill="none" stroke="#fff" stroke-width="3"/></svg>Anaerobic capacity.</li>
    </ul>
  </section>

  <div class="price-badge">
    <span class="amount">£100</span>
    <span class="detail">for the full course*<br>+ free training T-Shirt</span>
    <span class="note">*6 weeks</span>
  </div>

  <section class="details">
    <div class="detail-bar">
      <span class="label">WHEN?</span>
      <span class="value">Starting Friday 3rd October<br>@6pm-7pm<small>(Then every following Friday)</small></span>
    </div>
    <div class="detail-bar">
      <span class="label">WHERE?</span>
      <span class="value">Harwick Grange<br>Athletics Track</span>
    </div>
  </section>

  <section class="booking">
    <p class="cta">to book or for further<br>information please <strong>contact us</strong></p>
    <ul class="contact-list">
      <li><svg viewBox="0 0 20 20"><rect x="2" y="4" width="16" height="12" fill="none" stroke="#d4202a" stroke-width="2"/><path d="M2 5l8 6 8-6" fill="none" stroke="#d4202a" stroke-width="2"/></svg>contact@briskfieldacademy.co.uk</li>
      <li><svg viewBox="0 0 20 20"><rect x="5" y="1" width="10" height="18" rx="2" fill="none" stroke="#d4202a" stroke-width="2"/><circle cx="10" cy="15.5" r="1.2" fill="#d4202a"/></svg>07700914386</li>
      <li><svg viewBox="0 0 20 20"><circle cx="10" cy="10" r="8" fill="none" stroke="#d4202a" stroke-width="2"/><ellipse cx="10" cy="10" rx="3.5" ry="8" fill="none" stroke="#d4202a" stroke-width="1.5"/><path d="M2 10h16" stroke="#d4202a" stroke-width="1.5"/></svg>www.briskfieldacademy.com</li>
    </ul>
  </section>

  <div class="photo-action" role="img" aria-label="Photo of a junior rugby tackle during a match"></div>
</div>
</body>
</html>
```